Lena Hartwell Web

Lena Hartwell is a singer/songwriter that has a presence in the market for over 20 years. She currently has a website, lenahartwell.example that needs a major makeover. IT needs to be reorganized to; 1) make it more user friendly; 2) enable multi-languages including; Spanish, French, Russian, Japanese, Chinese and Portuguese; 3) enable purchases online through a storefront of promotional merchandise and music tracks. She has a logo that needs an update, as well as we currently have a business card open on PixelBazaar for input. Working to re-brand, or refresh her brand.

Lena Hartwell is the next Rosa Delmont! She has 5 platinum records, Lumen Award nominations and tours with Harold Prescott globally and is Nora Vandermeer's key backup singer for 12 years.
Updates

Some common questions have come up.  Here is some further input:

1) Colors - No specific color in mind but probably earth tones.  Although at this point we''re completely open.  Mary likes classical style, Russian, French decor.  Paris architecture. Greek, Italian textures, Goddess like symbols from the Roman Empire, or the symbols and pomp of the British monarchy.  One name on tap for the new CD is "Lanterns Over Quiet Water"
2) Example website - I have not found a new one specifically, but what I don''t like about the existing one is it is not easy to navigate.  Needs to be streamlined and easy to navigate with a storefront for merchandise and music downloads.  
3) On Logo - We''re revamping a "Global" merchandise rollout logo.  We''ve also considered possibly modifying the old english "Hartwell" family crest which signifies royalty, but have not explored that too much.  The hexagon yellow logo on her current website, I was thinking of modifying to gold (brushed - or polished?), then taking the LH lettering using a fountain pen type look there the line thickness flows with pressure on the pen, then make the gold look like a pillow, with the letter making an impression into the gold pillow.  This expands to a high quality pin, blinged up broach with diamonds imbedded for example, Global label identity, tee shirts, label tag on fashion clothing etc etc. 
 4) One thing marketing has asked us to build is a routine video blog to reach out to fans in a personal way.  Short clips of daily activity, travel prep for shows, etc. Possibly a signup/fanpage where people get emails sent back whenever anything new is posted, like a video blog, new pics, new events.  A menu to choose what you get updates on. 

Thanks, Dennis

Target Market(s)

1) Fan base in Europe, Asia, Latin America and North America
2) Movie producers seeking soundtracks
3) Private clients seeking an outstanding performer for corporate events

Industry/Entity Type

Singer

Requirements
Must have
• Better organization into smaller pages. Items critical include: 1) music tracks, 2) ClipStream links, 3) photos & Video, 4) storefront to enable online merchandise purchase 5) a way to illustrate her genre from; gospel, to rock, funk, R&B, country,

```html
<!DOCTYPE html>
<html lang="en">
<head>
<meta charset="utf-8">
<title>Lena Hartwell — Home</title>
<link href="https://fonts.googleapis.com/css2?family=Montserrat:wght@500&family=Questrial&display=swap" rel="stylesheet">
<style>
  :root {
    --ink: #000000;
    --gold: #f5c400;
    --white: #ffffff;
    --grey-text: #cfcfcf;
    --field: #c8c8c8;
    --panel: #ffffff;
    --panel-line: #e4e4e4;
    --panel-text: #333333;
    --accent-orange: #f26b1d;
    --share-blue: #3a66b0;
    --share-sky: #4fb5e8;
  }
  * { box-sizing: border-box; margin: 0; padding: 0; }
  html, body { width: 988px; height: 1200px; overflow: hidden; background: var(--ink); }
  body { position: relative; font-family: "Questrial", Arial, sans-serif; color: var(--white); }
  .abs { position: absolute; }

  .hero-photo {
    left: 0; top: 0; width: 988px; height: 580px;
    background:
      radial-gradient(ellipse at 55% 35%, #5a5a5a 0%, #2a2a2a 40%, #111 75%),
      #111;
  }
  .hero-fade { left: 0; top: 500px; width: 988px; height: 80px; background: linear-gradient(#0000, #000); }

  .main-nav { left: 57px; top: 15px; display: flex; font-size: 12px; }
  .main-nav a { color: var(--white); text-decoration: none; margin-right: 16px; }
  .main-nav a.is-current { color: var(--gold); }

  .language-flags { left: 668px; top: 6px; display: flex; gap: 12px; }
  .language-flags svg { width: 34px; height: 21px; display: block; }

  .brand { left: 45px; top: 38px; width: 270px; text-align: center; }
  .brand-disc { width: 188px; height: 188px; border-radius: 50%; background: var(--gold); margin: 0 auto; }
  .brand-name { font-size: 29px; letter-spacing: 1px; color: var(--white); margin-top: 10px; }

  .updates { left: 668px; top: 58px; width: 300px; }
  .updates h2 { font-family: "Montserrat", sans-serif; font-weight: 500; color: var(--gold); font-size: 34px; letter-spacing: 2px; margin-bottom: 14px; }
  .update-title { color: var(--gold); font-size: 22px; line-height: 24px; }
  .update-date { font-size: 14px; margin: 6px 0 24px; }
  .updates-more { left: 668px; top: 466px; color: var(--gold); font-size: 22px; letter-spacing: 1px; }

  .share { right: 48px; top: 530px; display: flex; align-items: center; gap: 5px; font-size: 14px; }
  .share .net { background: var(--share-blue); padding: 5px 4px; font-size: 8px; line-height: 14px; }
  .share .net.alt { background: var(--share-sky); }

  .section-title { font-family: "Montserrat", sans-serif; font-weight: 500; font-size: 21px; letter-spacing: 1px; }
  .more-link { font-family: "Montserrat", sans-serif; font-weight: 500; font-size: 19px; letter-spacing: 1px; }

  .music-panel { left: 55px; top: 625px; width: 396px; height: 290px; background: var(--panel); padding: 7px 20px; color: var(--panel-text); font-size: 8px; }
  .player-head { display: flex; gap: 8px; height: 100px; }
  .player-art { width: 95px; height: 95px; background: linear-gradient(135deg, #6b4a3a, #2c2320); }
  .player-info { flex: 1; position: relative; }
  .play-dot { width: 24px; height: 24px; border-radius: 50%; background: var(--accent-orange); position: absolute; left: 0; top: 4px; }
  .play-dot::after { content: ""; position: absolute; left: 9px; top: 6px; border-left: 9px solid #fff; border-top: 6px solid transparent; border-bottom: 6px solid transparent; }
  .player-meta { position: absolute; left: 30px; top: 5px; line-height: 11px; }
  .player-meta .muted { color: #999; }
  .player-brand { position: absolute; right: 0; top: 4px; color: #999; font-size: 7px; }
  .waveform { position: absolute; left: 0; right: 0; top: 44px; height: 36px;
    background: repeating-linear-gradient(90deg, #9a9a9a 0 2px, #ddd 2px 3px); clip-path: polygon(0 60%,10% 30%,25% 45%,40% 20%,55% 40%,70% 25%,85% 45%,100% 35%,100% 100%,0 100%); }
  .track-list { list-style: none; margin-top: 2px; }
  .track-list li { display: flex; align-items: center; height: 18px; border-top: 1px solid var(--panel-line); font-weight: bold; white-space: nowrap; }
  .track-list li i { width: 12px; height: 12px; background: #8a6e5a; margin-right: 4px; flex: none; }
  .track-list li span.count { margin-left: auto; color: #999; font-weight: normal; }
  .panel-foot { display: flex; gap: 6px; align-items: center; margin-top: 8px; }
  .panel-foot i { width: 22px; height: 22px; background: #8a6e5a; }
  .like-row { margin-top: 6px; display: flex; gap: 3px; align-items: center; }
  .like-row b { background: #4a67a8; color: #fff; padding: 1px 4px; }

  .video-frame { left: 466px; top: 634px; width: 475px; height: 280px; background: #111; }
  .video-photo { position: absolute; left: 0; top: 22px; width: 475px; height: 224px; background: radial-gradient(ellipse at 40% 40%, #7d5a7a, #3a2f6a 55%, #161630); }
  .video-title { position: absolute; left: 8px; top: 3px; font-size: 14px; }
  .video-play { position: absolute; left: 204px; top: 112px; width: 66px; height: 46px; border-radius: 10px; background: rgba(20,20,20,.85); }
  .video-play::after { content: ""; position: absolute; left: 26px; top: 14px; border-left: 16px solid #fff; border-top: 9px solid transparent; border-bottom: 9px solid transparent; }
  .video-bar { position: absolute; left: 0; bottom: 0; width: 475px; height: 34px; background: #1b1b1b; font-size: 11px; display: flex; align-items: center; gap: 14px; padding: 0 14px; }
  .video-bar .brand-tag { margin-left: auto; color: #aaa; }

  .footer-links { list-style: none; font-size: 15px; color: var(--gold); line-height: 23.5px; }
  .footer-links li::before { content: "• "; }
  .footer-heading { color: var(--gold); font-size: 15px; }

  .newsletter { left: 461px; top: 1018px; width: 260px; font-size: 11px; }
  .newsletter .row { display: flex; align-items: center; height: 22px; }
  .newsletter label { width: 60px; }
  .newsletter .field { width: 155px; height: 12px; background: var(--field); }
  .newsletter .select { width: 48px; height: 13px; background: var(--field); color: #000; font-size: 10px; padding-left: 3px; position: relative; }
  .newsletter .select::after { content: ""; position: absolute; right: 4px; top: 4px; border-top: 5px solid #000; border-left: 4px solid transparent; border-right: 4px solid transparent; }
  .newsletter .submit { display: inline-block; margin-top: 6px; background: #ddd; color: #000; font-size: 9px; padding: 1px 4px; border: 1px solid #999; }

  .connect-icons { left: 725px; top: 1043px; width: 200px; display: flex; justify-content: center; gap: 3px; font-size: 8px; }
  .connect-icons span { padding: 2px 2px; }

  .copyright { left: 56px; top: 1159px; font-size: 10px; color: var(--grey-text); }
</style>
</head>
<body>
  <div class="abs hero-photo" role="img" aria-label="Black and white concert photo of the singer on stage with microphone stands and stage lights"></div>
  <div class="abs hero-fade"></div>

  <nav class="abs main-nav">
    <a class="is-current" href="#">HOME</a><a href="#">EVENTS</a><a href="#">SHOP</a><a href="#">MUSIC</a><a href="#">VIDEO</a><a href="#">PICTURES</a><a href="#">ABOUT ME</a><a href="#">DISCOGRAPHY</a>
  </nav>

  <div class="abs language-flags" aria-label="Languages">
    <svg viewBox="0 0 34 21" aria-label="English"><rect width="34" height="21" fill="#fff"/><g fill="#c8102e"><rect y="0" width="34" height="3"/><rect y="6" width="34" height="3"/><rect y="12" width="34" height="3"/><rect y="18" width="34" height="3"/></g><rect width="15" height="11" fill="#2b3a8c"/></svg>
    <svg viewBox="0 0 34 21" aria-label="Spanish"><rect width="34" height="21" fill="#c60b1e"/><rect y="5" width="34" height="11" fill="#ffc400"/></svg>
    <svg viewBox="0 0 34 21" aria-label="Russian"><rect width="34" height="7" fill="#fff"/><rect y="7" width="34" height="7" fill="#1c3fa8"/><rect y="14" width="34" height="7" fill="#d52b1e"/></svg>
    <svg viewBox="0 0 34 21" aria-label="French"><rect width="12" height="21" fill="#1f3fa0"/><rect x="12" width="11" height="21" fill="#fff"/><rect x="23" width="11" height="21" fill="#e1222a"/></svg>
    <svg viewBox="0 0 34 21" aria-label="Japanese"><rect width="34" height="21" fill="#fff"/><circle cx="17" cy="10.5" r="6" fill="#bc002d"/></svg>
    <svg viewBox="0 0 34 21" aria-label="Chinese"><rect width="34" height="21" fill="#de2910"/><circle cx="7" cy="6" r="3" fill="#ffde00"/></svg>
    <svg viewBox="0 0 34 21" aria-label="Portuguese"><rect width="14" height="21" fill="#046a38"/><rect x="14" width="20" height="21" fill="#da291c"/><circle cx="14" cy="10.5" r="4" fill="#ffe900"/></svg>
  </div>

  <div class="abs brand">
    <div class="brand-disc"></div>
    <div class="brand-name">LENA HARTWELL</div>
  </div>

  <section class="abs updates">
    <h2>UPDATES:</h2>
    <div class="update-title">CRESCENT PALACE<br>with Nora Vandermeer</div>
    <div class="update-date">January 10 - Atlantic City, NJ</div>
    <div class="update-title">BROOKFIELD P.A.C. with<br>Nora Vandermeer</div>
    <div class="update-date">January 11 - Durham, NC</div>
    <div class="update-title">ASHGROVE Coliseum<br>Memorial Auditorium<br>with Nora Vandermeer</div>
    <div class="update-date">January 12 - Greensboro, NC</div>
  </section>
  <div class="abs updates-more">MORE UPDATES...</div>

  <div class="abs share">Share: <span class="net">FriendHub</span><span class="net alt">Chirper</span></div>

  <h3 class="abs section-title" style="left:55px;top:592px">LATEST MUSIC</h3>
  <h3 class="abs section-title" style="left:466px;top:592px">LATEST VIDEOS</h3>

  <div class="abs music-panel">
    <div class="player-head">
      <div class="player-art" role="img" aria-label="Album cover photo of two artists"></div>
      <div class="player-info">
        <div class="play-dot"></div>
        <div class="player-meta"><span class="muted">Lena Hartwell</span><br>Lena Hartwell - Golden Hour</div>
        <div class="player-brand">WAVENEST</div>
        <div class="waveform"></div>
      </div>
    </div>
    <ul class="track-list">
      <li><i></i>Lena Hartwell - Lena Hartwell - Golden Hour<span class="count">▶ 556</span></li>
      <li><i></i>Lena Hartwell - Lena Hartwell - Letters Unsent<span class="count">▶ 748</span></li>
      <li><i></i>Lena Hartwell - Lena Hartwell - Coastline Dreaming<span class="count">▶ 695</span></li>
      <li><i></i>Lena Hartwell - Night Owl Allstars &amp; Lena Hartwell - Paper Moons<span class="count">▶ 553</span></li>
      <li><i></i>Lena Hartwell - Lena Hartwell - Still Standing Tall<span class="count">▶ 371</span></li>
      <li><i></i>Lena Hartwell - Marco Feldgate feat. Lena Hartwell - Take Me Somewhere Warm<span class="count">▶ 334</span></li>
      <li><i></i>Lena Hartwell - Lena Hartwell - Velvet Night Live Session<span class="count">▶ 513</span></li>
    </ul>
    <div class="panel-foot"><i></i><span>Lena Hartwell<br><b>Lena Hartwell Recordings</b></span></div>
    <div class="like-row"><b>Like</b><b>Share</b> 15 people like this.</div>
  </div>

  <div class="abs video-frame">
    <div class="video-title">Lena Hartwell Live at the House of Velvet</div>
    <div class="video-photo" role="img" aria-label="Live performance still of the singer with microphone under blue and purple stage lights"></div>
    <div class="video-play"></div>
    <div class="video-bar"><span>▶</span><span>0:00 / 5:04</span><span class="brand-tag">ClipStream</span></div>
  </div>

  <div class="abs more-link" style="left:55px;top:926px">MORE...</div>
  <div class="abs more-link" style="left:468px;top:926px">MORE...</div>

  <ul class="abs footer-links" style="left:56px;top:985px">
    <li>ONLINE STORE</li><li>WAVENEST</li><li>ON TOUR</li><li>PHOTO GALLERY</li><li>MUSIC</li>
  </ul>
  <ul class="abs footer-links" style="left:244px;top:985px">
    <li>VIDEOS</li><li>FANFAGE</li><li>EVENTS</li><li>STREAMING MUSIC</li>
  </ul>

  <div class="abs footer-heading" style="left:461px;top:989px">NEWSLETTERS</div>
  <form class="abs newsletter">
    <div class="row"><label>Name</label><div class="field"></div></div>
    <div class="row"><label>Last Name</label><div class="field"></div></div>
    <div class="row"><label>Email</label><div class="field"></div></div>
    <div class="row"><label>I'm</label><div class="select">Male</div></div>
    <span class="submit">Subscribe Now!</span>
  </form>

  <div class="abs footer-heading" style="left:758px;top:989px">CONNECT WITH US</div>
  <div class="abs connect-icons"><span>CircleNet</span><span>FriendHub</span><span>Chirper</span><span>ClipStream</span></div>

  <div class="abs copyright">Lena Hartwell Copyright 2014 All Rights Reserved · Privacy Policy · Terms &amp; Conditions</div>
</body>
</html>
```